"White Paper" for Brightpath Studies, LLC

Hi there! I'm creating a short white paper for my business that people will download from my website (not yet launched) in PDF format. I want to create this document in Word and manage/finalize the text myself. I have created a primitive Word document (using mostly filler text) that shows the elements of this White Paper, and the design elements that need to be done, including: 1) making the cover look good; 2) choosing fonts; 3) creating several design elements such as a pull quotes and a bullet "how to tell" box; 4) creating a table of contents page; 5) making the photos (included) look good - you may process and size them anyway you like, but please include these photos in the sections they are already in (and know these photos are free to use); 6) designing section headers; and a few other misc. tasks.

The deliverable back from you is a word file (can be a straight doc or a template, whichever you think best) that I will be able to modify and use myself. Of course, until I buy your design, you can post it in a form that I can see but not manipulate. But know that when I buy it, I want a Word document.

Tight turnaround for this - need it done in 2 days. Email me with questions. Thank you.

Target Market(s)

Parents of K-12 children in the USA.

Industry/Entity Type

Education

Font styles to use
Sans Serif

Colors
3276b5
b768aa
d2a4cc
85abd2

Requirements
Must have
• Clean design that projects my credibility
• Flexibility so I can change text and some elements (such as size of pull quotes and the "How to Tell" text box
• Final product must be delivered to me in a Microsoft Word file that I can modify myself

```html
<!DOCTYPE html>
<html lang="en">
<head>
<meta charset="utf-8">
<title>Quick Guide – Making the Final Decision</title>
<link rel="stylesheet" href="https://fonts.googleapis.com/css2?family=Roboto:wght@400;700;900&display=swap">
<style>
  :root {
    --teal: #4aaec8;
    --paper: #ffffff;
    --desk: #cfd3d8;
    --ink: #333333;
    --photo-light: #c6dbef;
    --photo-mid: #a8c6e2;
  }
  * { box-sizing: border-box; margin: 0; padding: 0; }
  html, body {
    width: 1200px; height: 727px; overflow: hidden;
    background: var(--desk);
    font-family: "Roboto", Arial, sans-serif;
  }
  .spread { position: relative; width: 1200px; height: 727px; }
  .page {
    position: absolute; top: 14px; width: 500px; height: 707px;
    background: var(--paper);
    box-shadow: 0 1px 4px rgba(0,0,0,.25);
    overflow: hidden;
  }
  .page--cover { left: 95px; }
  .page--contents { left: 605px; }

  /* Cover */
  .cover-band {
    position: absolute; left: 0; top: 0; width: 500px; height: 577px;
    background: var(--teal);
  }
  .cover-photo {
    position: absolute; left: 130px; top: 45px; width: 370px; height: 532px;
    background:
      linear-gradient(to bottom, rgba(255,255,255,0) 84%, #ffffff 100%),
      linear-gradient(to bottom, var(--photo-mid) 0%, var(--photo-light) 45%, var(--photo-mid) 100%);
  }
  .cover-title {
    position: absolute; left: 35px; top: 138px;
    color: #ffffff; font-weight: 700; font-size: 66px; line-height: 71px;
  }
  .cover-subtitle {
    position: absolute; left: 0; top: 588px; width: 500px;
    text-align: center; color: var(--teal);
  }
  .cover-subtitle__lead { font-weight: 700; font-size: 24.5px; line-height: 27px; }
  .cover-subtitle__line { font-weight: 400; font-size: 23.5px; line-height: 26px; }

  /* Contents */
  .contents-heading {
    position: absolute; left: 60px; top: 228px;
    color: var(--teal); font-weight: 700; font-size: 30px;
  }
  .contents-list {
    position: absolute; left: 90px; top: 299px; width: 308px;
    list-style: none; font-size: 13px; color: var(--ink);
  }
  .contents-list li {
    display: flex; align-items: baseline; height: 32.4px;
  }
  .contents-list .leader {
    flex: 1; margin: 0 1px; border-bottom: 1px dotted #555; transform: translateY(-3px);
  }
  .copyright {
    position: absolute; left: 0; top: 660px; width: 500px;
    text-align: center; font-size: 9px; color: var(--ink);
  }
  .page-number {
    position: absolute; left: 436px; top: 670px; font-size: 9px; color: #666;
  }
</style>
</head>
<body>
<main class="spread">
  <section class="page page--cover">
    <div class="cover-band"></div>
    <div class="cover-photo" role="img" aria-label="Portrait photo of the author in a light blue shirt, arms crossed"></div>
    <h1 class="cover-title">QUICK<br>GUIDE</h1>
    <div class="cover-subtitle">
      <p class="cover-subtitle__lead">MAKING THE FINAL DECISION</p>
      <p class="cover-subtitle__line">about which K-12 school</p>
      <p class="cover-subtitle__line">my child should attend</p>
    </div>
  </section>

  <section class="page page--contents">
    <h2 class="contents-heading">TABLE OF CONTENTS</h2>
    <ol class="contents-list">
      <li><span>1. Introduction</span><span class="leader"></span><span>3</span></li>
      <li><span>2. Teaching</span><span class="leader"></span><span>4</span></li>
      <li><span>3. Program</span><span class="leader"></span><span>6</span></li>
      <li><span>4. Culture</span><span class="leader"></span><span>8</span></li>
      <li><span>5. Where graduates go</span><span class="leader"></span><span>10</span></li>
      <li><span>6. Your family's needs</span><span class="leader"></span><span>11</span></li>
      <li><span>7. Making Tradeoffs</span><span class="leader"></span><span>12</span></li>
    </ol>
    <p class="copyright">Copyright 2017 Brightpath Studies, LLC®</p>
    <span class="page-number">2</span>
  </section>
</main>
</body>
</html>
```